Website Design for Australian Vocational Education organisation

A website for an Educational organisation. A responsive design that works well on a laptop desktop or a mobile phone. Is easy to navigate. Be able to start small and add new pages and features at a later stage.
Requires the logo, the name of company, home page with hero shots, enquiry form that forwards to a specified email address
links to social media, home page. We need a home page, and two more templates for sub pages.
Must not be a typical common design.

current website www.qlmv.edu.au
this needs to look different. logo should remain the same.

Target Market(s)

across age groups from 18-70. so must be inutitive. some will be tech savvy and others not.

Industry/Entity Type

Education

Coding

Coded - Design and coding required

Colors

Designer to choose colors to be used in the design.

Requirements
Must have
• responsive design, video, photo gallery, hero image, social media links, news feed, calendar, shopping cart, enquiry form
Nice to have
• Sample website
• www.brightpathskills.com.au
• but should not be similar to this. it must look different. the sample is to give an idea on the various pages and links that will be required

```html
<!DOCTYPE html>
<html lang="en">
<head>
<meta charset="utf-8">
<title>Meridian Vale Academy of Skills</title>
<link rel="stylesheet" href="https://fonts.googleapis.com/css2?family=Lato:wght@400;700&family=Montserrat:wght@500;600;700&display=swap">
<style>
:root{
  --navy:#1f2456;
  --navy-deep:#141a4a;
  --red:#d0102c;
  --red-dark:#b50d27;
  --grey-bg:#f0f0f0;
  --text:#3a3a4a;
  --muted:#666;
  --white:#fff;
}
*{box-sizing:border-box;margin:0;padding:0}
html,body{width:1200px;height:3632px;overflow:hidden}
body{position:relative;font-family:'Lato',sans-serif;color:var(--text);background:var(--white)}
.abs{position:absolute}
h1,h2,h3,.nav-item,.btn{font-family:'Montserrat',sans-serif}

/* top bar */
.topbar{left:0;top:0;width:1200px;height:42px;background:var(--navy);color:var(--white)}
.topbar .call{position:absolute;left:158px;top:10px;font-size:13px}
.topbar .call b{font-size:18px;font-weight:600;margin-left:4px}
.social-dots{position:absolute;right:160px;top:14px;display:flex;gap:30px}
.social-dots span{width:13px;height:13px;border-radius:50%;background:var(--white)}

/* header */
.header{left:0;top:42px;width:1200px;height:102px;background:var(--white);border-bottom:1px solid #e3e3e3}
.brand{position:absolute;left:162px;top:18px;display:flex;align-items:center;gap:10px}
.brand-mark{width:66px;height:66px;background:var(--navy)}
.brand-name{font-family:'Montserrat',sans-serif;font-weight:700;font-size:13px;line-height:16px;color:var(--red);text-transform:uppercase}
.nav{position:absolute;left:405px;top:0;height:102px;display:flex}
.nav-item{height:102px;display:flex;flex-direction:column;align-items:center;justify-content:center;gap:10px;font-size:14px;font-weight:500;color:var(--navy-deep);border-right:1px solid #e3e3e3}
.nav-item svg{width:24px;height:24px}
.nav-item.active{background:var(--red);color:var(--white)}
.nav-item.cart{color:var(--red);border-right:none}

/* hero */
.hero{left:0;top:144px;width:1200px;height:605px}
.hero-title{left:0;top:180px;width:1200px;text-align:center;color:var(--white);font-size:38px;font-weight:500;line-height:42px}
.hero-sub{left:0;top:280px;width:1200px;text-align:center;color:var(--white);font-size:20px}
.btn{display:flex;align-items:center;justify-content:center;background:var(--red);color:var(--white);font-weight:500}
.hero-btn{left:503px;top:328px;width:190px;height:51px;font-size:17px}
.arrow{width:52px;height:52px;border-radius:50%;background:rgba(255,255,255,.8);display:flex;align-items:center;justify-content:center}

/* about */
.video{left:169px;top:804px;width:445px;height:285px;background:linear-gradient(120deg,#6b5a4c,#a89279 55%,#5c6770)}
.play{left:353px;top:908px;width:76px;height:76px;border-radius:50%;background:var(--white);display:flex;align-items:center;justify-content:center}
.about{left:654px;top:805px;width:380px}
.section-title{font-size:32px;font-weight:600;color:var(--navy)}
.about p{font-size:15px;line-height:25px;color:var(--text);margin-top:14px}
.about .btn{width:152px;height:42px;font-size:14px;margin-top:26px}

/* courses */
.courses-title{left:0;top:1282px;width:1182px;text-align:center;color:var(--white);font-size:28px;font-weight:600}
.course{width:210px;height:264px;background:rgba(60,10,40,.45);text-align:center;color:var(--white);padding-top:26px}
.course .ring{width:90px;height:90px;border:3px solid var(--white);border-radius:50%;margin:0 auto;display:flex;align-items:center;justify-content:center}
.course h3{font-size:16px;font-weight:600;margin-top:20px}
.course p{font-size:13.5px;line-height:21px;margin-top:8px;padding:0 18px}

/* gallery */
.gallery-title{left:0;top:1810px;width:1192px;text-align:center}
.ph{border:1px solid #ddd}

/* calendar & news */
.cal{left:163px;top:2471px;width:397px;height:329px;box-shadow:0 4px 12px rgba(0,0,0,.2);background:var(--navy-deep)}
.cal-head{height:48px;background:var(--white);display:flex;align-items:center;justify-content:center;gap:56px;font-family:'Montserrat',sans-serif;font-size:20px;font-weight:500;color:var(--red)}
.cal-head i{font-style:normal;color:#888;font-size:22px}
.cal-days,.cal-grid{display:grid;grid-template-columns:repeat(7,1fr)}
.cal-days{height:36px;background:var(--red);color:var(--white);font-size:12px;font-weight:700;align-items:center;text-align:center}
.cal-grid div{height:47px;display:flex;align-items:center;justify-content:center;color:var(--white);font-size:18px;font-weight:700;border-right:1px solid #2c3370;border-bottom:1px solid #2c3370}
.news{left:603px;width:440px;display:flex;gap:16px}
.news .thumb{width:122px;height:122px;border-radius:50%;flex:none;border:4px solid var(--white);box-shadow:0 2px 8px rgba(0,0,0,.15)}
.news small{font-size:12px;color:#333;display:block;margin-top:4px}
.news h4{font-size:18px;color:var(--navy);margin-top:4px;font-weight:700}
.news p{font-size:13.5px;line-height:22px;color:var(--muted);margin-top:4px}

/* enquiry */
.enq-title{left:0;top:2960px;width:1208px;text-align:center;color:var(--white);font-size:28px;font-weight:600}
.field{background:var(--white);border:1px solid #ddd;font-size:17px;color:#555;padding-left:18px;display:flex;align-items:center}
.submit{left:611px;top:3137px;width:401px;height:50px;background:var(--navy-deep);font-size:19px;font-weight:600}

/* footer */
.f-col{top:3360px}
.f-col h5{font-family:'Montserrat',sans-serif;font-size:18px;font-weight:500;color:var(--navy);border-left:3px solid var(--red);padding-left:8px}
.f-col ul{list-style:none;margin-top:8px;padding-left:11px}
.f-col li{font-size:14.5px;line-height:25px;color:var(--navy);white-space:nowrap}
.f-social{left:178px;top:3462px;display:flex;gap:30px}
.f-social span{width:14px;height:14px;border-radius:50%;background:var(--navy)}
.bottombar{left:0;top:3568px;width:1200px;height:64px;background:#e5e5e6;text-align:center;font-size:13px;color:#666;padding-top:28px}
</style>
</head>
<body>

<div class="abs topbar">
  <div class="call">CALL US <b>+61 400 555 012</b></div>
  <div class="social-dots" aria-label="Social media links"><span></span><span></span><span></span><span></span></div>
</div>

<header class="abs header">
  <div class="brand">
    <div class="brand-mark"></div>
    <div class="brand-name">Meridian Vale<br>Academy of<br>Skills</div>
  </div>
  <nav class="nav">
    <div class="nav-item active" style="width:107px">
      <svg viewBox="0 0 24 24" fill="none" stroke="#fff" stroke-width="2"><path d="M12 3a6 6 0 0 0-3 11v3h6v-3a6 6 0 0 0-3-11zM10 21h4"/></svg>ABOUT US</div>
    <div class="nav-item" style="width:108px">
      <svg viewBox="0 0 24 24" fill="none" stroke="#1f2456" stroke-width="2"><path d="M2 9l10-5 10 5-10 5zM6 11v5c3 3 9 3 12 0v-5"/></svg>COURSES</div>
    <div class="nav-item" style="width:113px">
      <svg viewBox="0 0 24 24" fill="#1f2456"><circle cx="9" cy="8" r="4"/><circle cx="17" cy="9" r="3"/><path d="M1 20c0-5 16-5 16 0zM15 20c0-3 8-4 8 0z"/></svg>STUDENTS</div>
    <div class="nav-item" style="width:84px">
      <svg viewBox="0 0 24 24" fill="none" stroke="#1f2456" stroke-width="2"><rect x="3" y="5" width="18" height="16"/><path d="M3 10h18M8 3v4M16 3v4"/></svg>NEWS</div>
    <div class="nav-item" style="width:138px">
      <svg viewBox="0 0 24 24" fill="#1f2456"><path d="M6 2l4 4-2 3c1 3 3 5 6 6l3-2 4 4-3 4C9 20 3 12 3 5z"/></svg>CONTACT US</div>
    <div class="nav-item cart" style="width:95px">
      <svg viewBox="0 0 24 24" fill="none" stroke="#d0102c" stroke-width="2"><path d="M2 3h3l3 12h11l2-8H6"/><circle cx="9" cy="20" r="1.5"/><circle cx="18" cy="20" r="1.5"/></svg>CART</div>
  </nav>
</header>

<section class="abs hero">
  <svg width="1200" height="605" class="abs" style="left:0;top:0" role="img" aria-label="Hero photo of smiling students working together at laptops">
    <defs><linearGradient id="heroG" x1="0" y1="0" x2="1" y2="1"><stop offset="0" stop-color="#4a4a52"/><stop offset=".5" stop-color="#6d6a68"/><stop offset="1" stop-color="#8a8784"/></linearGradient></defs>
    <path d="M0 0H1200V600C1100 600 1000 540 860 560 700 585 600 520 470 525 320 532 200 560 110 545 60 538 30 555 0 560Z" fill="url(#heroG)"/>
    <path d="M0 0H1200V600C1100 600 1000 540 860 560 700 585 600 520 470 525 320 532 200 560 110 545 60 538 30 555 0 560Z" fill="rgba(30,30,40,.35)"/>
  </svg>
  <h1 class="abs hero-title">WELCOME TO MERIDIAN VALE<br>ACADEMY OF ADVANCED SKILLS</h1>
  <div class="abs hero-sub">Lorem ipsum dolor sit amet consectetuer adipiscing elit</div>
  <div class="abs btn hero-btn">ENQUIRY NOW</div>
  <div class="abs arrow" style="left:129px;top:248px"><svg width="20" height="20" viewBox="0 0 20 20"><path d="M13 3l-7 7 7 7" stroke="#222" stroke-width="2.5" fill="none"/></svg></div>
  <div class="abs arrow" style="left:1017px;top:248px"><svg width="20" height="20" viewBox="0 0 20 20"><path d="M7 3l7 7-7 7" stroke="#222" stroke-width="2.5" fill="none"/></svg></div>
</section>

<div class="abs video" role="img" aria-label="Video still of a smiling hospitality student in a cafe apron"></div>
<div class="abs play"><svg width="30" height="30" viewBox="0 0 30 30"><path d="M8 4l18 11-18 11z" fill="#111"/></svg></div>
<div class="abs about">
  <h2 class="section-title">ABOUT MVAS</h2>
  <p>Pellentesque faucibus Ut accumsan ultricies elit Maecenas at justo id velit placerat molestie</p>
  <p>Aaculis aliquam Mauris nunc est nunc venenatis in tristique eu imperdiet ac nisl Cum sociis natoque penatibus et magnis dis parturient montes nascetur ridiculus mus In iaculis facilisis</p>
  <div class="btn">LEARN MORE</div>
</div>

<svg class="abs" style="left:0;top:1160px" width="1200" height="640">
  <defs><linearGradient id="courseG" x1="0" y1="0" x2="1" y2="0"><stop offset="0" stop-color="#c8102e"/><stop offset=".55" stop-color="#5a1c48"/><stop offset="1" stop-color="#22245a"/></linearGradient></defs>
  <path d="M0 40C120 20 200 0 300 30 420 70 520 40 640 50 800 65 880 130 1000 110 1080 95 1140 70 1200 55V600C1100 630 960 610 860 585 700 545 560 560 420 545 260 525 120 520 0 550Z" fill="#e0aeba"/>
  <path d="M0 70C120 50 220 40 320 70 440 105 540 60 660 70 800 85 900 150 1010 135 1090 122 1150 100 1200 70V560C1100 620 960 610 860 580 700 530 560 540 420 525 260 505 120 500 0 540Z" fill="url(#courseG)"/>
</svg>
<h2 class="abs courses-title">OUR COURSES</h2>
<div class="abs course" style="left:160px;top:1340px">
  <div class="ring"><svg width="44" height="44" viewBox="0 0 44 44" fill="#fff"><circle cx="22" cy="16" r="5"/><circle cx="13" cy="12" r="3"/><circle cx="31" cy="12" r="3"/><path d="M6 22l8 14h16l8-14-6 4-10 4-10-4z"/></svg></div>
  <h3>ANIMAL CARE</h3><p>Morbi tincidunt erat ac purus commodo interdum erat feugiat lectus</p>
</div>
<div class="abs course" style="left:383px;top:1392px">
  <div class="ring"><svg width="44" height="44" viewBox="0 0 44 44" fill="none" stroke="#fff" stroke-width="2.5"><rect x="6" y="14" width="32" height="22" rx="2"/><path d="M16 14v-5h12v5M6 24h32"/></svg></div>
  <h3>BUSINESS</h3><p>Morbi tincidunt erat ac purus commodo interdum erat feugiat lectus</p>
</div>
<div class="abs course" style="left:610px;top:1340px">
  <div class="ring"><svg width="48" height="44" viewBox="0 0 48 44" fill="none" stroke="#fff" stroke-width="2.5"><path d="M4 10h16c3 0 4 2 4 4v22c0-2-1-3-4-3H4zM44 10H28c-3 0-4 2-4 4v22c0-2 1-3 4-3h16z"/></svg></div>
  <h3>EDUCTION</h3><p>Morbi tincidunt erat ac purus commodo interdum erat feugiat lectus</p>
</div>
<div class="abs course" style="left:836px;top:1392px">
  <div class="ring"><svg width="44" height="44" viewBox="0 0 44 44" fill="#fff"><path d="M12 12c0-6 20-6 20 0z"/><circle cx="22" cy="18" r="6"/><path d="M8 40c0-10 28-10 28 0z"/></svg></div>
  <h3>HOSPITALITY</h3><p>Morbi tincidunt erat ac purus commodo interdum erat feugiat lectus</p>
</div>

<h2 class="abs section-title gallery-title">PHOTO GALLERY</h2>
<div class="abs ph" style="left:162px;top:1882px;width:334px;height:353px;background:linear-gradient(135deg,#8d8f94,#c9c7c2 50%,#7b8190)" role="img" aria-label="Students studying around a round table, seen from above"></div>
<div class="abs ph" style="left:507px;top:1882px;width:172px;height:171px;background:linear-gradient(160deg,#6a8fc8,#2a3f7a)" role="img" aria-label="Graduates throwing caps into a blue sky"></div>
<div class="abs ph" style="left:687px;top:1882px;width:353px;height:171px;background:linear-gradient(180deg,#7e8a9a,#5d6b55 60%,#9bb070)" role="img" aria-label="Students sitting on a bench with laptops"></div>
<div class="abs ph" style="left:507px;top:2065px;width:172px;height:170px;background:linear-gradient(135deg,#7a6452,#b89d84)" role="img" aria-label="Two smiling students in a library"></div>
<div class="abs ph" style="left:687px;top:2065px;width:171px;height:170px;background:linear-gradient(135deg,#c4b4a3,#5a7aa8)" role="img" aria-label="Smiling student holding blue folders"></div>
<div class="abs ph" style="left:867px;top:2065px;width:173px;height:170px;background:linear-gradient(135deg,#a7a9ad,#6f7d93)" role="img" aria-label="Group of students reviewing documents"></div>

<svg class="abs" style="left:0;top:2290px" width="1200" height="640">
  <path d="M0 60C150 40 300 10 480 40 620 65 720 20 820 30 950 45 1050 120 1200 20V640H0Z" fill="var(--grey-bg)"/>
  <path d="M560 38C680 18 760 20 880 45 980 65 1060 120 1200 20V60C1060 150 970 90 880 70 780 48 700 30 560 38Z" fill="var(--navy-deep)"/>
</svg>

<h2 class="abs section-title" style="left:166px;top:2408px;font-size:28px">CALENDAR</h2>
<div class="abs cal">
  <div class="cal-head"><i>‹</i>AUG 2019<i>›</i></div>
  <div class="cal-days"><span>MO</span><span>TU</span><span>WE</span><span>TH</span><span>FR</span><span>SA</span><span>SU</span></div>
  <div class="cal-grid">
    <div>1</div><div>2</div><div>3</div><div>4</div><div>5</div><div>6</div><div>7</div>
    <div>8</div><div>9</div><div>10</div><div>11</div><div>12</div><div>13</div><div>14</div>
    <div>15</div><div>16</div><div>17</div><div>18</div><div>19</div><div>20</div><div>21</div>
    <div>22</div><div>23</div><div>24</div><div>25</div><div>26</div><div>27</div><div>28</div>
    <div>29</div><div>30</div><div>31</div><div></div><div></div><div></div><div></div>
  </div>
</div>

<h2 class="abs section-title" style="left:607px;top:2408px;font-size:28px">LATEST NEWS</h2>
<div class="abs news" style="top:2480px">
  <div class="thumb" style="background:linear-gradient(135deg,#3f5f9a,#c9c4b8)" role="img" aria-label="Student writing in a notebook"></div>
  <div><small>10 Aug 2019</small><h4>Pellentesque faucibus</h4><p>accumsan ultricies elit Maecenas at justo id velit placerat molestie Donec dictum lectus non odio Cras a ante vitae</p></div>
</div>
<div class="abs news" style="top:2648px">
  <div class="thumb" style="background:linear-gradient(135deg,#2d3568,#c89c7c)" role="img" aria-label="Smiling student wearing glasses"></div>
  <div style="padding-left:4px"><small>04 Aug 2019</small><h4>Nunc tempus felis vitae</h4><p>accumsan ultricies elit Maecenas at justo id velit placerat molestie Donec dictum lectus non odio Cras a ante vitae</p></div>
</div>

<svg class="abs" style="left:0;top:2850px" width="1200" height="446" role="img" aria-label="Red tinted background photo of students">
  <defs><linearGradient id="enqG" x1="0" y1="0" x2="1" y2="1"><stop offset="0" stop-color="#c8102e"/><stop offset=".5" stop-color="#dc1f3c"/><stop offset="1" stop-color="#c30d2a"/></linearGradient></defs>
  <path d="M0 40C200 20 360 -10 480 30 620 70 720 10 860 20 1000 30 1100 0 1200 -10V446H0Z" fill="url(#enqG)"/>
  <path d="M0 40C200 20 360 -10 480 30 620 70 720 10 860 20 1000 30 1100 0 1200 -10V10C1100 20 1000 45 860 40 720 35 620 90 480 50 360 15 200 45 0 65Z" fill="var(--navy-deep)"/>
</svg>
<h2 class="abs enq-title">ENQUIRY FORM</h2>
<div class="abs field" style="left:201px;top:3017px;width:401px;height:50px">Your Name</div>
<div class="abs field" style="left:201px;top:3077px;width:401px;height:50px">Email address</div>
<div class="abs field" style="left:201px;top:3137px;width:401px;height:50px">Phone</div>
<div class="abs field" style="left:611px;top:3017px;width:401px;height:111px;align-items:flex-start;padding-top:14px">Message</div>
<div class="abs btn submit">SUBMIT NOW</div>

<div class="abs brand" style="left:174px;top:3364px">
  <div class="brand-mark"></div>
  <div class="brand-name">Meridian Vale<br>Academy of<br>Skills</div>
</div>
<div class="abs f-social" aria-label="Social media links"><span></span><span></span><span></span><span></span></div>
<div class="abs f-col" style="left:398px"><h5>QUICK LINKS</h5><ul><li>Home</li><li>About Us</li><li>Services</li><li>Courses</li><li>Students</li></ul></div>
<div class="abs f-col" style="left:577px"><h5>SITEMAP</h5><ul><li>Support</li><li>News</li><li>Enquiry Now</li><li>Blogs</li><li>News</li></ul></div>
<div class="abs f-col" style="left:746px"><h5>CONTACT US</h5><ul><li>18 Wattle Grove, Kingsford ACT 2600</li><li>Mon - Fri 8.30 AM - 04.30 PM</li><li>+61 400 555 012</li><li>hello@meridianvale-skills.example</li></ul></div>

<div class="abs bottombar">© 2019 Company Name All right reserved</div>

</body>
</html>
```